Poster Design For Obstacle Run

Design a poster for the Crow Ridge Obstacle run.
Text: Crow Ridge Obstacle Run. May 12th, 2018. Sittard. www.crowridgedash.nl. I have added a lot of pictures.
Furthermore, the logo should be included. As an example I included a poster from the ironbark race that we really like (ironbark team challenge) and also. Feel free to take a look at our website for inspiration: www.crowridgedash.nl

```html
<!DOCTYPE html>
<html lang="en">
<head>
<meta charset="utf-8">
<title>Crow Ridge Obstacle Run – Poster</title>
<link rel="stylesheet" href="https://fonts.googleapis.com/css2?family=Black+Ops+One&family=Ubuntu:wght@700&display=swap">
<style>
  :root {
    --page: #ffffff;
    --sand-top: #efd69f;
    --sand-mid: #f3c46a;
    --sand-bottom: #f8b535;
    --ink: #1c140c;
    --paper: #ffffff;
    --accent: #e85a1e;
    --mud-light: #c9a456;
    --mud-dark: #6b5330;
    --sky-blue: #3e5c78;
  }
  html, body {
    margin: 0;
    width: 1200px;
    height: 1200px;
    overflow: hidden;
    background: var(--page);
  }
  .poster {
    position: absolute;
    left: 176px;
    top: 0;
    width: 848px;
    height: 1200px;
    overflow: hidden;
    background: linear-gradient(180deg, var(--sand-top) 0%, var(--sand-mid) 55%, var(--sand-bottom) 100%);
  }
  .photo-strips {
    position: absolute;
    inset: 0;
    width: 848px;
    height: 1200px;
  }
  .event-mark {
    position: absolute;
    left: 580px;
    top: 600px;
    width: 240px;
    display: flex;
    align-items: center;
    gap: 10px;
  }
  .event-mark__dot {
    flex: none;
    width: 34px;
    height: 34px;
    border-radius: 50%;
    background: var(--accent);
  }
  .event-mark__name {
    font-family: "Black Ops One", sans-serif;
    font-size: 30px;
    line-height: 1;
    color: var(--accent);
    text-transform: uppercase;
  }
  .headline {
    position: absolute;
    left: 0;
    top: 738px;
    width: 848px;
    margin: 0;
    font-family: "Black Ops One", sans-serif;
    font-weight: 400;
    color: var(--ink);
    text-align: center;
    text-transform: uppercase;
    line-height: 1;
  }
  .headline__line {
    display: block;
  }
  .headline__line--top { font-size: 100px; letter-spacing: 2px; }
  .headline__line--bottom { font-size: 104px; margin-top: 2px; letter-spacing: 1px; }
  .date-band {
    position: absolute;
    left: 68px;
    top: 960px;
    width: 720px;
    height: 104px;
  }
  .date-band__brush {
    position: absolute;
    inset: 0;
    width: 100%;
    height: 100%;
  }
  .date-band__text {
    position: absolute;
    left: 0;
    right: 0;
    top: 22px;
    margin: 0;
    text-align: center;
    font-family: "Black Ops One", sans-serif;
    font-size: 54px;
    color: var(--paper);
    text-transform: uppercase;
    line-height: 1;
  }
  .web-address {
    position: absolute;
    left: 0;
    right: 0;
    top: 1108px;
    margin: 0;
    text-align: center;
    font-family: "Ubuntu", sans-serif;
    font-weight: 700;
    font-size: 50px;
    color: var(--ink);
    letter-spacing: 0.5px;
  }
</style>
</head>
<body>
  <main class="poster">
    <svg class="photo-strips" viewBox="0 0 848 1200" role="img" aria-label="Photographs: a runner in a red shirt splashing through a muddy pool, and a muddy arm with a watch gripping a wall while climbing">
      <defs>
        <linearGradient id="climbTone" x1="0" y1="0" x2="1" y2="1">
          <stop offset="0" stop-color="#2c2a28"/>
          <stop offset="0.45" stop-color="var(--sky-blue)"/>
          <stop offset="1" stop-color="#8b8577"/>
        </linearGradient>
        <linearGradient id="mudTone" x1="0" y1="0" x2="1" y2="1">
          <stop offset="0" stop-color="var(--mud-light)"/>
          <stop offset="0.5" stop-color="#b98f45"/>
          <stop offset="1" stop-color="var(--mud-dark)"/>
        </linearGradient>
      </defs>
      <path class="photo-strips__climb" fill="url(#climbTone)"
        d="M250 0 H848 V540 L820 532 L790 545 L760 520 L700 500 L650 470 L610 452 L560 430 L520 420 L495 395 L470 370 L440 330 L400 300 L360 260 L330 220 L300 180 L280 140 L300 130 L270 100 L290 80 L260 50 L280 30 Z"/>
      <path class="photo-strips__splash" fill="url(#mudTone)"
        d="M0 112 L120 118 L220 140 L320 180 L400 215 L470 255 L520 290 L555 325 L590 360 L600 400 L625 430 L600 450 L610 480 L580 500 L600 530 L570 560 L585 590 L550 620 L545 660 L520 690 L495 720 L440 705 L380 680 L300 660 L200 645 L100 635 L0 625 Z"/>
    </svg>

    <div class="event-mark">
      <span class="event-mark__dot"></span>
      <span class="event-mark__name">Crow Ridge Obstacle Run</span>
    </div>

    <h1 class="headline">
      <span class="headline__line headline__line--top">Crow Ridge</span>
      <span class="headline__line headline__line--bottom">Obstacle Run</span>
    </h1>

    <div class="date-band">
      <svg class="date-band__brush" viewBox="0 0 720 104" preserveAspectRatio="none" aria-hidden="true">
        <path fill="var(--ink)"
          d="M6 14 L80 8 L200 4 L360 0 L520 6 L660 4 L716 12 L710 30 L718 50 L712 70 L718 88 L690 96 L560 100 L400 98 L240 104 L100 98 L10 96 L2 80 L10 60 L0 40 L8 26 Z"/>
      </svg>
      <p class="date-band__text">May 12th, 2018</p>
    </div>

    <p class="web-address">www.crowridgedash.nl.</p>
  </main>
</body>
</html>
```